Belvoro Website

I need a website for a startup company that provides GIS (Geographic Information Services) staffing and products for local cities. Current website is www.belvorogroup.com

```html
<!DOCTYPE html>
<html lang="en">
<head>
<meta charset="utf-8">
<title>Belvoro Group</title>
<link href="https://fonts.googleapis.com/css2?family=Merriweather:wght@400;700&family=Montserrat:wght@400;500&family=Poppins:wght@400;500;600&family=Roboto:wght@400;500&display=swap" rel="stylesheet">
<style>
:root{
  --blue:#1f6aad;
  --blue-dark:#175893;
  --ink:#111111;
  --text:#222222;
  --muted:#555555;
  --white:#ffffff;
  --line:#d9d9d9;
  --footer:#000000;
}
*{margin:0;padding:0;box-sizing:border-box}
html,body{width:1200px;height:2871px;overflow:hidden;background:var(--white)}
body{position:relative;font-family:'Montserrat',sans-serif;color:var(--text)}
.abs{position:absolute}
.serif{font-family:'Merriweather',serif}
.btn{position:absolute;display:flex;align-items:center;justify-content:center;background:var(--blue);color:var(--white);border-radius:24px;font-family:'Merriweather',serif;font-weight:700;font-size:16px;box-shadow:0 3px 6px rgba(0,0,0,.18)}

/* header */
.site-header{position:absolute;left:0;top:0;width:1200px;height:87px;background:var(--white)}
.brand{left:110px;top:22px;font-family:'Merriweather',serif;font-weight:700;font-size:29px;color:var(--ink)}
.nav a{position:absolute;top:34px;font-family:'Merriweather',serif;font-size:16px;color:var(--ink);text-decoration:none}
.nav a.active{color:var(--blue);font-weight:700;text-decoration:underline}

/* hero */
.hero{position:absolute;left:0;top:87px;width:1200px;height:539px}
.hero-title{left:109px;top:180px;font-family:'Merriweather',serif;font-weight:700;font-size:58px;color:var(--white)}
.hero-sub{left:113px;top:256px;font-size:18px;font-weight:500;color:var(--white)}

/* about */
.section-title{position:absolute;left:0;width:1200px;text-align:center;font-family:'Merriweather',serif;font-weight:700;font-size:34px;color:var(--ink)}
.section-title span{color:var(--blue)}
.about-frame{left:122px;top:780px;width:459px;height:342px;border:3px solid #cfcfcf}
.about-corner{left:99px;top:760px;width:140px;height:95px;background:var(--blue)}
.about-photo{left:110px;top:769px;width:455px;height:338px;background:linear-gradient(135deg,#6b5c44 0%,#8a8070 40%,#4b5a66 70%,#2f3a44 100%)}
.about-lead{left:633px;top:778px;width:455px;font-size:15.5px;line-height:29px;font-weight:500;color:var(--ink)}
.about-body{left:633px;top:927px;width:455px;font-size:15px;line-height:29px;color:var(--muted)}

/* services */
.services{position:absolute;left:0;top:1219px;width:1200px;height:644px;background:radial-gradient(ellipse at 50% 40%,#2575ba 0%,var(--blue) 55%,var(--blue-dark) 100%)}
.services .section-title{color:var(--white);top:72px}
.card{position:absolute;background:var(--white);border-radius:4px}
.card-img{position:absolute;left:16px;top:15px;right:16px;height:189px;border-radius:3px}
.card-icon{position:absolute;top:175px;width:64px;height:64px;border-radius:50%;background:var(--white);display:flex;align-items:center;justify-content:center}
.card-title{position:absolute;left:0;right:0;top:242px;text-align:center;font-family:'Merriweather',serif;font-weight:700;font-size:20px;color:var(--ink)}
.card-title.hl{color:var(--blue)}
.feat{position:absolute;font-family:'Roboto',sans-serif;font-size:15px;color:var(--ink);display:flex;align-items:center;gap:4px}

/* contact */
.info-icon{position:absolute;left:135px;width:80px;height:80px;border-radius:50%;background:var(--blue);display:flex;align-items:center;justify-content:center}
.info-label{position:absolute;left:243px;font-family:'Roboto',sans-serif;font-weight:500;font-size:15px;color:var(--ink)}
.info-text{position:absolute;left:243px;font-family:'Roboto',sans-serif;font-size:15px;line-height:26px;color:var(--ink)}
.field{position:absolute;background:var(--white);box-shadow:0 2px 10px rgba(0,0,0,.12);font-family:'Roboto',sans-serif;font-size:14px;color:#666;padding:17px 17px}

/* footer */
.site-footer{position:absolute;left:0;top:2443px;width:1200px;height:428px;background:var(--footer);color:var(--white)}
.foot-brand{left:116px;top:68px;font-family:'Merriweather',serif;font-weight:700;font-size:33px}
.social{position:absolute;top:132px;width:29px;height:29px;border-radius:50%;background:var(--blue)}
.foot-head{position:absolute;top:60px;font-family:'Poppins',sans-serif;font-weight:600;font-size:21px}
.foot-link{position:absolute;font-family:'Poppins',sans-serif;font-size:15px;display:flex;align-items:center;gap:10px}
.news-text{left:812px;top:110px;width:290px;font-family:'Poppins',sans-serif;font-size:15px;line-height:31px}
.news-email{left:814px;top:191px;font-family:'Poppins',sans-serif;font-size:15px}
.news-line{left:814px;top:211px;width:270px;height:2px;background:var(--white)}
.foot-divider{left:99px;top:365px;width:1002px;height:1px;background:#6b6b6b}
.copyright{left:0;top:385px;width:1200px;text-align:center;font-family:'Poppins',sans-serif;font-size:15px}
</style>
</head>
<body>

<header class="site-header">
  <div class="abs brand">Belvoro Group</div>
  <nav class="nav">
    <a class="active" href="#" style="left:646px">Home</a>
    <a href="#" style="left:738px">About Us</a>
    <a href="#" style="left:851px">Services</a>
  </nav>
  <div class="btn" style="left:946px;top:20px;width:140px;height:47px">Contact Us</div>
</header>

<section class="hero">
  <svg class="abs" style="left:0;top:0" width="1200" height="539" viewBox="0 0 1200 539">
    <defs>
      <linearGradient id="mapTone" x1="0" y1="0" x2="1" y2="1">
        <stop offset="0" stop-color="#3a3a3a"/><stop offset=".5" stop-color="#262626"/><stop offset="1" stop-color="#1a1a1a"/>
      </linearGradient>
      <linearGradient id="officeTone" x1="0" y1="0" x2="1" y2="1">
        <stop offset="0" stop-color="#6f8a62"/><stop offset=".45" stop-color="#8b8a7a"/><stop offset="1" stop-color="#4a4036"/>
      </linearGradient>
    </defs>
    <rect role="img" aria-label="Dark aerial city map background" width="1200" height="539" fill="url(#mapTone)"/>
    <path role="img" aria-label="GIS analyst reviewing a large map on screen in an office" d="M724 0 Q520 270 718 539 L1200 539 L1200 0 Z" fill="url(#officeTone)"/>
    <path d="M718 0 Q506 270 708 539" fill="none" stroke="#ffffff" stroke-width="12"/>
  </svg>
  <div class="abs hero-title">Belvoro Group</div>
  <div class="abs hero-sub">We Make GIS Work For You</div>
  <div class="btn" style="left:112px;top:302px;width:141px;height:46px">Get Started</div>
</section>

<section>
  <h2 class="section-title" style="top:695px">About <span>Belvoro Group</span></h2>
  <div class="abs about-corner"></div>
  <div class="abs about-frame"></div>
  <div class="abs about-photo" role="img" aria-label="Smiling GIS specialist at a desk with map displays on monitors"></div>
  <p class="abs about-lead">We are an innovative team of geospatial experts with 25 years of experience in the field of GIS. We specialize in providing results-driven GIS solutions for local government and the private sector.</p>
  <p class="abs about-body">Duis aute irure dolor in reprehenderit in voluptate velit esse cillum dolore eu fugiat nulla pariatur. Excepteur sint occaecat cupidatat non proident, sunt in culpa qui officia deserunt mollit anim id est laborum.</p>
  <div class="btn" style="left:631px;top:1064px;width:141px;height:47px">Read More</div>
</section>

<section class="services">
  <h2 class="section-title">Our Services</h2>

  <div class="card" style="left:111px;top:145px;width:291px;height:294px">
    <div class="card-img" role="img" aria-label="Consultant pointing at a large city map display" style="background:linear-gradient(120deg,#6d8a6a,#a08a9a 45%,#2c2c30)"></div>
    <div class="card-icon" style="left:114px">
      <svg width="36" height="40" viewBox="0 0 36 40" fill="none" stroke="#1f6aad" stroke-width="1.6"><rect x="5" y="3" width="26" height="34" rx="2"/><path d="M11 20l7-4 7 4-7 4z M11 25l7 4 7-4 M11 30l7 4 7-4"/><rect x="2" y="7" width="14" height="7" fill="#fff"/><path d="M4 10h10"/></svg>
    </div>
    <div class="card-title">GIS Consulting</div>
  </div>

  <div class="card" style="left:427px;top:145px;width:346px;height:405px">
    <div class="card-img" role="img" aria-label="Glowing circuit board with GIS lettering" style="background:radial-gradient(ellipse at 50% 50%,#d0454a 0%,#2a3f7a 45%,#0f1d3a 100%)"></div>
    <div class="card-icon" style="left:141px">
      <svg width="40" height="40" viewBox="0 0 40 40" fill="none" stroke="#1f6aad" stroke-width="1.6"><path d="M20 4a8 8 0 0 1 8 8c0 6-8 14-8 14s-8-8-8-14a8 8 0 0 1 8-8z"/><circle cx="20" cy="12" r="3"/><path d="M4 28l16-6 16 6-16 8z M12 31l16-6"/></svg>
    </div>
    <div class="card-title hl">GIS Applications</div>
    <div class="feat" style="left:31px;top:287px"><svg width="14" height="14" viewBox="0 0 14 14"><circle cx="7" cy="7" r="7" fill="#1f6aad"/><path d="M3.8 7.2l2.2 2.2 4.2-4.4" stroke="#fff" stroke-width="1.6" fill="none"/></svg>MapCore Online</div>
    <div class="feat" style="left:181px;top:287px"><svg width="14" height="14" viewBox="0 0 14 14"><circle cx="7" cy="7" r="7" fill="#1f6aad"/><path d="M3.8 7.2l2.2 2.2 4.2-4.4" stroke="#fff" stroke-width="1.6" fill="none"/></svg>MapCore Enterprise</div>
    <div class="feat" style="left:30px;top:319px"><svg width="14" height="14" viewBox="0 0 14 14"><circle cx="7" cy="7" r="7" fill="#1f6aad"/><path d="M3.8 7.2l2.2 2.2 4.2-4.4" stroke="#fff" stroke-width="1.6" fill="none"/></svg>Dashboards</div>
    <div class="feat" style="left:172px;top:319px"><svg width="14" height="14" viewBox="0 0 14 14"><circle cx="7" cy="7" r="7" fill="#1f6aad"/><path d="M3.8 7.2l2.2 2.2 4.2-4.4" stroke="#fff" stroke-width="1.6" fill="none"/></svg>Portal Builder</div>
    <div class="feat" style="left:109px;top:352px"><svg width="14" height="14" viewBox="0 0 14 14"><circle cx="7" cy="7" r="7" fill="#1f6aad"/><path d="M3.8 7.2l2.2 2.2 4.2-4.4" stroke="#fff" stroke-width="1.6" fill="none"/></svg>Custom widgets</div>
  </div>

  <div class="card" style="left:797px;top:145px;width:291px;height:294px">
    <div class="card-img" role="img" aria-label="Map with red location pins in front of city lights" style="background:linear-gradient(180deg,#8a6a3a 0%,#4a3a2a 35%,#2a3440 70%,#1a2028 100%)"></div>
    <div class="card-icon" style="left:114px">
      <svg width="40" height="40" viewBox="0 0 40 40" fill="none" stroke="#1f6aad" stroke-width="1.6"><rect x="6" y="5" width="22" height="8" rx="2"/><rect x="6" y="15" width="22" height="8" rx="2"/><rect x="6" y="25" width="22" height="8" rx="2"/><circle cx="10" cy="9" r="1"/><circle cx="10" cy="19" r="1"/><circle cx="10" cy="29" r="1"/><path d="M31 22a5 5 0 0 1 5 5c0 4-5 9-5 9s-5-5-5-9a5 5 0 0 1 5-5z" fill="#fff"/></svg>
    </div>
    <div class="card-title">Spatial Data Solutions</div>
  </div>
</section>

<section>
  <h2 class="section-title" style="top:1948px">Contact <span>Us</span></h2>

  <div class="info-icon" style="top:2040px">
    <svg width="40" height="40" viewBox="0 0 40 40" fill="none" stroke="#fff" stroke-width="2.4"><path d="M20 5a9 9 0 0 1 9 9c0 7-9 16-9 16s-9-9-9-16a9 9 0 0 1 9-9z"/><circle cx="20" cy="14" r="3.5"/><path d="M8 30c0 3 5 5 12 5s12-2 12-5"/></svg>
  </div>
  <div class="info-label" style="top:2046px">ADDRESS:</div>
  <div class="info-text" style="top:2070px">4180 N. Lindley Ave. #208<br>Ashford, CA 90217</div>

  <div class="info-icon" style="top:2144px">
    <svg width="40" height="40" viewBox="0 0 40 40"><path d="M11 6l6 1 2 8-4 3c2 4 5 7 9 9l3-4 8 2 1 6c-1 3-4 4-7 4C17 34 6 23 6 11c0-3 2-5 5-5z" fill="#fff"/><path d="M24 7a10 10 0 0 1 9 9 M24 12a5 5 0 0 1 4 4" stroke="#fff" stroke-width="2" fill="none"/></svg>
  </div>
  <div class="info-label" style="top:2160px">PHONE:</div>
  <div class="info-text" style="top:2184px">+1 555 014 2290</div>

  <div class="info-icon" style="top:2246px">
    <svg width="40" height="30" viewBox="0 0 40 30"><rect x="2" y="2" width="36" height="26" rx="3" fill="#fff"/><path d="M3 4l17 13L37 4" stroke="#1f6aad" stroke-width="3" fill="none"/></svg>
  </div>
  <div class="info-label" style="top:2262px">EMAIL:</div>
  <div class="info-text" style="top:2286px">info@belvorogroup.com</div>

  <div class="field" style="left:481px;top:2041px;width:283px;height:49px">First Name</div>
  <div class="field" style="left:775px;top:2041px;width:283px;height:49px">Last Name</div>
  <div class="field" style="left:481px;top:2103px;width:283px;height:49px">Phone Number</div>
  <div class="field" style="left:775px;top:2103px;width:283px;height:49px">Email</div>
  <div class="field" style="left:481px;top:2167px;width:577px;height:111px">Message</div>
  <div class="btn" style="left:481px;top:2298px;width:133px;height:47px;font-family:'Roboto',sans-serif;font-weight:500;font-size:18px">Submit</div>
</section>

<footer class="site-footer">
  <div class="abs foot-brand">Belvoro Group</div>
  <div class="social" style="left:124px" role="img" aria-label="Social profile"></div>
  <div class="social" style="left:170px" role="img" aria-label="Social profile"></div>
  <div class="social" style="left:215px" role="img" aria-label="Social profile"></div>
  <div class="social" style="left:261px" role="img" aria-label="Social profile"></div>

  <div class="foot-head" style="left:423px">Quick Links</div>
  <div class="foot-link" style="left:425px;top:97px"><svg width="15" height="14" viewBox="0 0 15 14"><path d="M1 7h11M7 2l5 5-5 5" stroke="#fff" stroke-width="2.4" fill="none"/></svg><span style="font-weight:500">Home</span></div>
  <div class="foot-link" style="left:425px;top:129px"><svg width="15" height="14" viewBox="0 0 15 14"><path d="M1 7h11M7 2l5 5-5 5" stroke="#fff" stroke-width="2.4" fill="none"/></svg>About Us</div>
  <div class="foot-link" style="left:425px;top:161px"><svg width="15" height="14" viewBox="0 0 15 14"><path d="M1 7h11M7 2l5 5-5 5" stroke="#fff" stroke-width="2.4" fill="none"/></svg>Services</div>
  <div class="foot-link" style="left:425px;top:194px"><svg width="15" height="14" viewBox="0 0 15 14"><path d="M1 7h11M7 2l5 5-5 5" stroke="#fff" stroke-width="2.4" fill="none"/></svg>Contact&nbsp; Us</div>

  <div class="foot-head" style="left:614px">Other Links</div>
  <div class="foot-link" style="left:615px;top:97px"><svg width="15" height="14" viewBox="0 0 15 14"><path d="M1 7h11M7 2l5 5-5 5" stroke="#fff" stroke-width="2.4" fill="none"/></svg>FAQ</div>
  <div class="foot-link" style="left:615px;top:128px"><svg width="15" height="14" viewBox="0 0 15 14"><path d="M1 7h11M7 2l5 5-5 5" stroke="#fff" stroke-width="2.4" fill="none"/></svg>Tems of Use</div>
  <div class="foot-link" style="left:615px;top:159px"><svg width="15" height="14" viewBox="0 0 15 14"><path d="M1 7h11M7 2l5 5-5 5" stroke="#fff" stroke-width="2.4" fill="none"/></svg>Privacy Policy</div>
  <div class="foot-link" style="left:615px;top:190px"><svg width="15" height="14" viewBox="0 0 15 14"><path d="M1 7h11M7 2l5 5-5 5" stroke="#fff" stroke-width="2.4" fill="none"/></svg>Support Links</div>
  <div class="foot-link" style="left:615px;top:221px"><svg width="15" height="14" viewBox="0 0 15 14"><path d="M1 7h11M7 2l5 5-5 5" stroke="#fff" stroke-width="2.4" fill="none"/></svg>Conditions</div>

  <div class="foot-head" style="left:811px">Sign Up To Newsletter</div>
  <p class="abs news-text">Lorem ipsum dolor sit amet,consectetur adipiscing elit,adipiscing elit.</p>
  <div class="abs news-email">Email</div>
  <div class="abs news-line"></div>
  <div class="btn" style="left:819px;top:242px;width:145px;height:50px;font-family:'Poppins',sans-serif;font-weight:600;font-size:17px;border-radius:26px">Subscribe</div>

  <div class="abs foot-divider"></div>
  <div class="abs copyright">Copyrights@2024.Belvoro Group.All Rights Reserved</div>
</footer>

</body>
</html>
```